Business Card for Business consulting practice

Need a design for a consultant business card. Simple and elegant.
I need the following information on the card:
Logo: (see uploaded file)
Company name: Calmora Advisory Group
Name: Dana Weltrup
Title: Managing Director - Aerospace and Defence
Phone #: 514-268-3917
e-mail: dana.weltrup@calmora-example.com
Website: www.calmora-example.com
Tagline: Proposals Management and Capture support for complex procurements

```html
<!DOCTYPE html>
<html lang="en">
<head>
<meta charset="utf-8">
<title>Calmora Advisory Group – Business Card</title>
<link rel="stylesheet" href="https://fonts.googleapis.com/css2?family=Cinzel:wght@400;600&family=Arimo:wght@400;700&display=swap">
<style>
  :root {
    --navy: #0a2d42;
    --teal: #1f8db8;
    --white: #ffffff;
    --ink: #111111;
    --backdrop: #e9e4e2;
  }
  * { margin: 0; padding: 0; box-sizing: border-box; }
  html, body { width: 1200px; height: 960px; overflow: hidden; }
  body { background: var(--backdrop); position: relative; font-family: "Arimo", Arial, sans-serif; }

  .card { position: absolute; left: 254px; width: 674px; height: 386px; overflow: hidden; }

  /* Front */
  .card--front { top: 46px; background: var(--navy); }
  .brand { position: absolute; left: 0; right: 0; text-align: center; font-family: "Cinzel", serif; font-weight: 400; }
  .card--front .brand { top: 140px; color: var(--white); }
  .brand__name { display: block; font-size: 68px; line-height: 1; letter-spacing: 1px; }
  .brand__group { display: block; font-size: 18px; letter-spacing: 6px; margin-top: 14px; color: var(--teal); }
  .services {
    position: absolute; left: 0; right: 0; top: 346px;
    text-align: center; font-family: "Cinzel", serif; font-size: 13.5px; line-height: 20px;
    color: var(--teal); letter-spacing: 0.3px; white-space: nowrap;
  }
  .services span + span::before { content: "|"; margin: 0 8px; }

  /* Back */
  .card--back { top: 507px; height: 383px; width: 672px; background: var(--white); border: 6px solid var(--navy); }
  .card--back .brand { left: 30px; right: auto; width: 284px; top: 158px; color: var(--navy); }
  .card--back .brand__name { font-size: 44px; font-weight: 600; letter-spacing: 0; }
  .card--back .brand__group { font-size: 12px; letter-spacing: 4px; margin-top: 8px; }

  .divider { position: absolute; left: 330px; top: 93px; width: 3px; height: 188px; background: var(--navy); }
  .person { position: absolute; left: 352px; top: 66px; }
  .person__name { font-family: "Cinzel", serif; font-weight: 600; font-size: 22px; color: var(--navy); letter-spacing: 0.5px; }
  .person__title { font-weight: 700; font-size: 13px; color: var(--teal); margin-top: 6px; }

  .contacts { position: absolute; left: 344px; top: 170px; list-style: none; }
  .contacts li { display: flex; align-items: center; height: 28px; margin-bottom: 14.5px; font-size: 15px; color: var(--ink); white-space: nowrap; }
  .contacts svg { width: 28px; height: 28px; margin-right: 18px; flex: none; }

  .tagline {
    position: absolute; left: 0; right: 0; bottom: 8px; text-align: center;
    font-family: "Cinzel", serif; font-weight: 600; font-size: 13.5px; color: var(--navy); letter-spacing: 0.3px;
  }
</style>
</head>
<body>

<section class="card card--front" aria-label="Card front">
  <div class="brand">
    <span class="brand__name">CALMORA</span>
    <span class="brand__group">ADVISORY GROUP</span>
  </div>
  <p class="services">
    <span>Opportunity identification</span><span>Strategy &amp; Business Development</span><span>Bids &amp; Proposals</span>
  </p>
</section>

<section class="card card--back" aria-label="Card back">
  <div class="brand">
    <span class="brand__name">CALMORA</span>
    <span class="brand__group">ADVISORY GROUP</span>
  </div>

  <div class="divider"></div>

  <div class="person">
    <h1 class="person__name">Dana Weltrup</h1>
    <p class="person__title">Managing Director - Aerospace and Defence</p>
  </div>

  <ul class="contacts">
    <li>
      <svg viewBox="0 0 28 28" aria-hidden="true">
        <circle cx="14" cy="14" r="13" fill="none" stroke="#999" stroke-width="1"/>
        <path d="M10.5 8.5c.6-.6 1.4-.5 1.8.1l1 1.6c.3.5.2 1.1-.2 1.5l-.8.7c.6 1.4 1.7 2.6 3.1 3.2l.7-.8c.4-.4 1-.5 1.5-.2l1.6 1c.6.4.7 1.2.1 1.8l-.7.7c-.8.8-2 .9-3 .4-2.8-1.4-4.9-3.5-6.3-6.3-.5-1-.4-2.2.4-3z" fill="var(--teal)"/>
      </svg>
      514-268-3917
    </li>
    <li>
      <svg viewBox="0 0 28 28" aria-hidden="true">
        <circle cx="14" cy="14" r="13" fill="none" stroke="#999" stroke-width="1"/>
        <text x="14" y="19" text-anchor="middle" font-family="Arimo, sans-serif" font-weight="700" font-size="15" fill="var(--teal)">@</text>
      </svg>
      dana.weltrup@calmora-example.com
    </li>
    <li>
      <svg viewBox="0 0 28 28" aria-hidden="true">
        <circle cx="14" cy="14" r="13" fill="none" stroke="#999" stroke-width="1"/>
        <g fill="none" stroke="var(--teal)" stroke-width="1.2">
          <circle cx="14" cy="14" r="6.5"/>
          <ellipse cx="14" cy="14" rx="3" ry="6.5"/>
          <path d="M7.5 14h13M8.5 10.8h11M8.5 17.2h11"/>
        </g>
      </svg>
      www.calmora-example.com
    </li>
  </ul>

  <p class="tagline">Proposals Management and Capture support for complex procurements</p>
</section>

</body>
</html>
```